Construction Company Cellar Horizon needs Business Card

I would like modern looking business card design. I am attaching logo of our company. Please include cell nr 302.481.7736 , email address cellarhorizon4u@mailvex.com, web : cellarhorizon4u.com, please also include wording: Specializing in finishing and remodeling basements. You can play with dark grey and orange colors or any ideas are welcome. Also include social media icons Chatterloop and NestFinder.

```html
<!DOCTYPE html>
<html lang="en">
<head>
<meta charset="utf-8">
<title>Cellar Horizon – Business Card</title>
<link rel="stylesheet" href="https://fonts.googleapis.com/css2?family=Oswald:wght@500;600&family=Roboto:wght@400;500&display=swap">
<style>
  :root {
    --backdrop: #bcbdbf;
    --card: #231f20;
    --orange: #ee5a2a;
    --white: #ffffff;
    --shadow: rgba(0, 0, 0, 0.35);
  }
  * { box-sizing: border-box; margin: 0; padding: 0; }
  html, body {
    width: 724px; height: 1200px; overflow: hidden;
    background: var(--backdrop);
  }
  .sheet { position: relative; width: 724px; height: 1200px; }
  .card {
    position: absolute; left: 89px; width: 547px; height: 311px;
    background: var(--card); border-radius: 30px;
    box-shadow: 0 3px 8px var(--shadow);
    overflow: hidden; color: var(--white);
    font-family: "Roboto", Arial, sans-serif;
  }
  .card--front { top: 89px; }
  .card--back { top: 459px; }
  .card--alt { top: 800px; }

  .brand-name {
    position: absolute; right: 32px; top: 108px;
    font-family: "Oswald", "Arial Narrow", sans-serif;
    font-weight: 600; font-size: 40px; line-height: 1;
    letter-spacing: 2px; text-transform: uppercase;
    color: var(--orange);
  }
  .contact-list {
    position: absolute; right: 30px; top: 219px;
    list-style: none; text-align: right;
  }
  .contact-list li {
    display: flex; align-items: center; justify-content: flex-end;
    gap: 8px; height: 22px;
    font-size: 13px; letter-spacing: 1.4px;
  }
  .contact-list svg { width: 14px; height: 14px; fill: var(--orange); flex: none; }

  .tagline { position: absolute; left: 0; right: 0; text-align: center; }
  .tagline__lead { font-size: 13px; letter-spacing: 1px; line-height: 1; }
  .tagline__main {
    font-family: "Oswald", "Arial Narrow", sans-serif;
    font-weight: 500; font-size: 21px; letter-spacing: 0.6px;
    color: var(--orange); text-transform: uppercase; line-height: 1;
    margin-top: 8px;
  }
  .card--back .tagline { top: 134px; }
  .card--alt .tagline { top: 206px; }
  .card--alt .tagline__main { margin-top: 6px; }

  .social {
    position: absolute; left: 0; right: 0;
    display: flex; justify-content: center; gap: 16px;
  }
  .card--back .social { top: 192px; }
  .card--alt .social { top: 257px; }
  .social__item {
    display: flex; align-items: center; gap: 6px;
    font-size: 11px; letter-spacing: 0.5px;
  }
  .social__dot { width: 18px; height: 18px; border-radius: 50%; background: var(--white); }

  .alt-name {
    position: absolute; left: 0; right: 0; top: 92px;
    text-align: center;
    font-family: "Oswald", "Arial Narrow", sans-serif;
    font-weight: 600; font-size: 40px; letter-spacing: 2px;
    text-transform: uppercase; color: var(--white); line-height: 1;
  }
</style>
</head>
<body>
<main class="sheet">

  <section class="card card--front" aria-label="Card front">
    <div class="brand-name">Cellar Horizon</div>
    <ul class="contact-list">
      <li>302.481.7736
        <svg viewBox="0 0 24 24" aria-hidden="true"><path d="M6.6 10.8a15.1 15.1 0 0 0 6.6 6.6l2.2-2.2c.3-.3.7-.4 1-.2 1.1.4 2.3.6 3.6.6.6 0 1 .4 1 1V20c0 .6-.4 1-1 1A17 17 0 0 1 3 4c0-.6.4-1 1-1h3.5c.6 0 1 .4 1 1 0 1.3.2 2.5.6 3.6.1.3 0 .7-.2 1z"/></svg>
      </li>
      <li>cellarhorizon4u@mailvex.com
        <svg viewBox="0 0 24 24" aria-hidden="true"><path d="M2 5h20v14H2z M2 5l10 8 10-8" stroke="#231f20" stroke-width="1.6"/></svg>
      </li>
      <li>cellarhorizon4u.com
        <svg viewBox="0 0 24 24" aria-hidden="true"><circle cx="12" cy="12" r="10"/><path d="M2 12h20M12 2v20M5 6h14M5 18h14M12 2c-5 5-5 15 0 20M12 2c5 5 5 15 0 20" stroke="#231f20" stroke-width="1.2" fill="none"/></svg>
      </li>
    </ul>
  </section>

  <section class="card card--back" aria-label="Card back">
    <div class="tagline">
      <p class="tagline__lead">specializing in</p>
      <p class="tagline__main">Finishing &amp; Remodeling Basements</p>
    </div>
    <div class="social">
      <span class="social__item"><span class="social__dot"></span>Chatterloop</span>
      <span class="social__item"><span class="social__dot"></span>NestFinder</span>
    </div>
  </section>

  <section class="card card--alt" aria-label="Card back, alternate">
    <div class="alt-name">Cellar Horizon</div>
    <div class="tagline">
      <p class="tagline__lead">specializing in</p>
      <p class="tagline__main">Finishing &amp; Remodeling Basements</p>
    </div>
    <div class="social">
      <span class="social__item"><span class="social__dot"></span>Chatterloop</span>
      <span class="social__item"><span class="social__dot"></span>NestFinder</span>
    </div>
  </section>

</main>
</body>
</html>
```